Quorvex - Automated robotic Inspection with AI need new business cards

We need a new design of our business cards. The company is focused on automated quality control at high speed with unmatched results. We have a logo but need a more forward leaning business card that shows that we are delivering cutting edge technology.

Contact Information for Business Card

Name
Position
Adress
Phone
Email
e.g.
Lena Holmqvist
Chief Financial Officer (CFO)

Quorvex Sweden AB
Bruksvägen 14, SE-175 43 JÄRFÄLLA, Sweden
Mobile: +46735 21 47 83 | Office: +46 8 61 94 27
www.quorvex-example.com

Font styles to use
Sans Serif

```html
<!DOCTYPE html>
<html lang="en">
<head>
<meta charset="utf-8">
<title>Quorvex – Business Card</title>
<link href="https://fonts.googleapis.com/css2?family=Nunito+Sans:wght@400;600;800&display=swap" rel="stylesheet">
<style>
  :root {
    --backdrop: #8c8c8e;
    --backdrop-dark: #6f6f71;
    --card: #2a2a2c;
    --ink: #f2f2f2;
    --ink-soft: #d6d6d6;
    --rule: #8a8a8a;
    --foil: #b8aa96;
  }
  * { margin: 0; padding: 0; box-sizing: border-box; }
  html, body { width: 1200px; height: 736px; overflow: hidden; }
  body {
    background: radial-gradient(ellipse at 45% 40%, var(--backdrop) 0%, var(--backdrop-dark) 100%);
    font-family: "Nunito Sans", sans-serif;
    position: relative;
  }
  .card {
    position: absolute;
    background: var(--card);
    box-shadow: 0 18px 40px rgba(0,0,0,.35);
  }
  /* Front side */
  .card-front {
    left: 90px; top: 218px;
    width: 500px; height: 300px;
    display: flex; align-items: center; justify-content: center; gap: 18px;
  }
  .brand-dot {
    width: 30px; height: 30px; border-radius: 50%;
    background: var(--foil);
  }
  .brand-name {
    color: var(--foil);
    font-weight: 800;
    font-size: 54px;
    letter-spacing: 6px;
    text-transform: uppercase;
  }
  /* Back side */
  .card-back {
    left: 720px; top: 118px;
    width: 300px; height: 500px;
    padding: 40px 34px 0 38px;
    color: var(--ink);
  }
  .card-back .brand {
    display: flex; align-items: center; gap: 10px;
    margin-bottom: 30px;
  }
  .card-back .brand-dot { width: 18px; height: 18px; }
  .card-back .brand-name { font-size: 30px; letter-spacing: 3px; }
  .person-name {
    font-weight: 800; font-size: 17px; letter-spacing: .5px;
    text-transform: uppercase;
  }
  .person-title {
    font-size: 13px; color: var(--ink-soft); margin-top: 2px;
    margin-bottom: 26px;
  }
  .contact-item { margin-bottom: 12px; }
  .contact-item .label { font-weight: 800; font-size: 13px; }
  .contact-item .value { font-size: 12.5px; color: var(--ink-soft); line-height: 1.4; }
  .contact-rule {
    width: 22px; height: 1px; background: var(--rule);
    margin: 0 0 12px;
  }
</style>
</head>
<body>
  <section class="card card-front" aria-label="Card front">
    <span class="brand-dot"></span>
    <span class="brand-name">Quorvex</span>
  </section>

  <section class="card card-back" aria-label="Card back">
    <div class="brand">
      <span class="brand-dot"></span>
      <span class="brand-name">Quorvex</span>
    </div>
    <p class="person-name">Lena Holmqvist</p>
    <p class="person-title">Chief Financial Officer (CFO)</p>

    <div class="contact-item">
      <p class="label">Office</p>
      <p class="value">+46 8 61 94 27</p>
    </div>
    <div class="contact-rule"></div>
    <div class="contact-item">
      <p class="label">Mobile</p>
      <p class="value">+46735 21 47 83</p>
    </div>
    <div class="contact-rule"></div>
    <div class="contact-item">
      <p class="label">Email</p>
      <p class="value">info@quorvex-example.com</p>
    </div>
    <div class="contact-rule"></div>
    <div class="contact-item">
      <p class="label">Web</p>
      <p class="value">www.quorvex-example.com</p>
    </div>
    <div class="contact-rule"></div>
    <div class="contact-item">
      <p class="label">Address</p>
      <p class="value">Quorvex Sweden AB<br>Bruksvägen 14, SE-175 43<br>JÄRFÄLLA, Sweden</p>
    </div>
  </section>
</body>
</html>
```